GlintOn Feather Line Toothbrush Backcard Design

We need a toothbrush backcard (toothbrush packaging) design for our new toothbrush. We are one of the leading toothbrush distributor and producer company. At the moment our toothbrushes are selling at Quinby, Kindred Mart, 4-Bright and many more supermarkets and mom-and-pop shops in Thailand. Our toothbrush is emphasized on the soft and slim tip bristles which will not hurt your enamel. Easy to grip handle that will ease of use. These 2 mains point should be communicated through the design.

Our brand name is GlintOn (see attached logo that you can use) and the toothbrush model is Feather Line. We will have 2 series for this model which are Feather Line Extra Soft and Feather Line Medium soft. They are basically differentiated by its packaging colors.

We are looking for the attractive and outstanding design from what available in the market right now. Please see enclosed die cut shape of the packaging. This backcard will hold 3 pieces of toothbrush with clear blister cover.

P.S We are very confident that our product produced with very good quality that's why we want to attract people to try. So when they walk in the aisle we want our toothbrush packaging to be eye catching and welcome customer to try.

Target Market(s)

B+ household consumers age between 18-65 both men and women who has open minded to the new product and willing to spend money without brand royalty.

Font styles to use
Sans Serif

Colors

Designer to choose colors to be used in the design.

Requirements
Must have
• - Logo, and model name
• - Quality mark as following GMP, FDA, ISO9001:2015, ISO22176
• - Attractive character which attract the target clients to try.
• - 2-sided packaging using attached die cut
Nice to have
Should not have
• What other brands have

```html
<!DOCTYPE html>
<html lang="en">
<head>
<meta charset="utf-8">
<title>GlintOn Feather Line Backcards</title>
<link href="https://fonts.googleapis.com/css2?family=Baloo+2:wght@600;700;800&display=swap" rel="stylesheet">
<style>
  :root {
    --page: #ffffff;
    --frame: #8a8a8a;
    --sun-top: #f9e51c;
    --sun-mid: #fbc928;
    --sun-low: #f7b733;
    --teal: #7fdacb;
    --blister: #2f8fd6;
    --label: #fcc31d;
    --ribbon: #fdf4c8;
    --ink: #353535;
    --white: #ffffff;
    --extra-a: #5d3f8e;
    --extra-b: #9a3f98;
    --extra-c: #d266ae;
    --medium-a: #2f3a8f;
    --medium-b: #2c4fb0;
    --medium-c: #1aa2e4;
  }
  * { margin: 0; padding: 0; box-sizing: border-box; }
  html, body { width: 828px; height: 1200px; overflow: hidden; background: var(--page); }
  .sheet {
    position: relative; width: 800px; height: 1160px;
    transform: scale(1.035); transform-origin: 0 0;
    border: 1px solid var(--frame);
    font-family: "Baloo 2", sans-serif;
  }
  .backcard { position: absolute; top: 44px; width: 364px; height: 1083px; overflow: hidden; }
  .backcard--extra { left: 26px; --accent: var(--extra-a); --base-a: var(--extra-a); --base-b: var(--extra-b); --base-c: var(--extra-c); }
  .backcard--medium { left: 412px; --accent: var(--medium-a); --base-a: var(--medium-a); --base-b: var(--medium-b); --base-c: var(--medium-c); }
  .backcard svg.art { position: absolute; inset: 0; }
  .series {
    position: absolute; left: 84px; top: 658px; width: 220px; height: 56px;
    background: var(--accent); border-radius: 28px;
    display: flex; align-items: center; padding-left: 16px; gap: 6px; color: var(--white);
  }
  .series-name { font-size: 14px; font-weight: 700; line-height: 15px; text-align: right; }
  .series-soft { font-size: 42px; font-weight: 800; font-style: italic; line-height: 1; margin-top: 4px; }
  .pack {
    position: absolute; left: 84px; top: 720px; width: 112px; height: 40px;
    background: var(--accent); border-radius: 20px;
    color: var(--white); font-size: 27px; font-weight: 800; font-style: italic;
    line-height: 42px; text-align: center;
  }
  .brand {
    position: absolute; left: 72px; top: 828px; width: 212px; text-align: center;
    color: var(--ink); font-size: 46px; font-weight: 800; line-height: 1;
  }
  .claim-text { font-family: "Baloo 2", sans-serif; font-weight: 800; fill: var(--ink); }
</style>
</head>
<body>
<div class="sheet">

  <div class="backcard backcard--extra">
    <svg class="art" width="364" height="1083" viewBox="0 0 364 1083">
      <defs>
        <linearGradient id="sunExtra" x1="0" y1="0" x2="0" y2="1">
          <stop offset="0" stop-color="var(--sun-top)"/><stop offset="0.35" stop-color="var(--sun-mid)"/><stop offset="1" stop-color="var(--sun-low)"/>
        </linearGradient>
        <linearGradient id="baseExtra" x1="0" y1="0" x2="1" y2="1">
          <stop offset="0" stop-color="var(--extra-a)"/><stop offset="0.5" stop-color="var(--extra-b)"/><stop offset="1" stop-color="var(--extra-c)"/>
        </linearGradient>
        <linearGradient id="brushExtra" x1="0" y1="0" x2="0" y2="1">
          <stop offset="0" stop-color="#ffffff" stop-opacity="0.95"/><stop offset="0.5" stop-color="#f2f4f4" stop-opacity="0.9"/><stop offset="0.62" stop-color="#8fdccd" stop-opacity="0.9"/><stop offset="1" stop-color="#f4f4f4" stop-opacity="0.9"/>
        </linearGradient>
      </defs>
      <rect class="sky" width="364" height="1083" fill="url(#sunExtra)"/>
      <path class="wave-band" d="M0,556 Q170,470 364,458 L364,1083 L0,1083 Z" fill="var(--teal)"/>
      <path class="wave-base" d="M0,582 Q170,494 364,480 L364,1083 L0,1083 Z" fill="url(#baseExtra)"/>
      <g class="blister" fill="none" stroke="var(--blister)" stroke-width="1.3">
        <rect x="11" y="18" width="360" height="1050" rx="30"/>
        <rect x="24" y="31" width="360" height="1024" rx="24"/>
        <rect x="146" y="78" width="230" height="52" rx="10"/>
        <path d="M164,110 q8,-14 16,0 q8,14 16,0 q8,-14 16,0 q8,14 16,0 L364,110"/>
      </g>
      <g role="img" aria-label="Three white toothbrushes with teal grips held under the clear blister">
        <rect x="54" y="200" width="80" height="890" rx="30" fill="url(#brushExtra)"/>
        <rect x="142" y="200" width="80" height="890" rx="30" fill="url(#brushExtra)"/>
        <rect x="230" y="200" width="80" height="890" rx="30" fill="url(#brushExtra)"/>
      </g>
      <rect class="label" x="70" y="646" width="216" height="300" rx="18" fill="var(--label)"/>
      <path class="ribbon" d="M70,810 L286,758 L286,838 L70,900 Z" fill="var(--ribbon)"/>
      <g class="claim">
        <path id="arcGripE" d="M89,912 A30,30 0 1 1 149,912" fill="none"/>
        <circle cx="119" cy="906" r="21" fill="var(--white)" stroke="var(--ink)" stroke-width="1.2"/>
        <rect x="104" y="909" width="30" height="4" rx="2" fill="none" stroke="var(--ink)"/>
        <rect x="104" y="901" width="9" height="7" fill="none" stroke="var(--ink)"/>
        <text class="claim-text" font-size="7.2"><textPath href="#arcGripE" startOffset="50%" text-anchor="middle">COMFORT GRIP HANDLE</textPath></text>
      </g>
      <g class="claim">
        <path id="arcTipE" d="M202,912 A30,30 0 1 1 262,912" fill="none"/>
        <circle cx="232" cy="906" r="21" fill="var(--white)" stroke="var(--ink)" stroke-width="1.2"/>
        <path d="M222,898 q10,-6 20,0 q2,10 -3,20 q-3,-6 -7,-6 q-4,0 -7,6 q-5,-10 -3,-20 Z" fill="none" stroke="var(--ink)" stroke-width="1.2"/>
        <text class="claim-text" font-size="6.4"><textPath href="#arcTipE" startOffset="50%" text-anchor="middle">SOFT &amp; SLIM TIP BRISTLES</textPath></text>
      </g>
    </svg>
    <div class="series"><div class="series-name">Feather Line<br>Extra</div><div class="series-soft">Soft</div></div>
    <div class="pack">3Pack</div>
    <div class="brand">GlintOn</div>
  </div>

  <div class="backcard backcard--medium">
    <svg class="art" width="364" height="1083" viewBox="0 0 364 1083">
      <defs>
        <linearGradient id="sunMedium" x1="0" y1="0" x2="0" y2="1">
          <stop offset="0" stop-color="var(--sun-top)"/><stop offset="0.35" stop-color="var(--sun-mid)"/><stop offset="1" stop-color="var(--sun-low)"/>
        </linearGradient>
        <linearGradient id="baseMedium" x1="0" y1="0" x2="1" y2="1">
          <stop offset="0" stop-color="var(--medium-a)"/><stop offset="0.5" stop-color="var(--medium-b)"/><stop offset="1" stop-color="var(--medium-c)"/>
        </linearGradient>
        <linearGradient id="brushMedium" x1="0" y1="0" x2="0" y2="1">
          <stop offset="0" stop-color="#ffffff" stop-opacity="0.95"/><stop offset="0.5" stop-color="#f2f4f4" stop-opacity="0.9"/><stop offset="0.62" stop-color="#8fdccd" stop-opacity="0.9"/><stop offset="1" stop-color="#f4f4f4" stop-opacity="0.9"/>
        </linearGradient>
      </defs>
      <rect class="sky" width="364" height="1083" fill="url(#sunMedium)"/>
      <path class="wave-band" d="M0,556 Q170,470 364,458 L364,1083 L0,1083 Z" fill="var(--teal)"/>
      <path class="wave-base" d="M0,582 Q170,494 364,480 L364,1083 L0,1083 Z" fill="url(#baseMedium)"/>
      <g class="blister" fill="none" stroke="var(--blister)" stroke-width="1.3">
        <rect x="11" y="18" width="360" height="1050" rx="30"/>
        <rect x="24" y="31" width="360" height="1024" rx="24"/>
        <rect x="146" y="78" width="230" height="52" rx="10"/>
        <path d="M164,110 q8,-14 16,0 q8,14 16,0 q8,-14 16,0 q8,14 16,0 L364,110"/>
      </g>
      <g role="img" aria-label="Three white toothbrushes with teal grips held under the clear blister">
        <rect x="54" y="200" width="80" height="890" rx="30" fill="url(#brushMedium)"/>
        <rect x="142" y="200" width="80" height="890" rx="30" fill="url(#brushMedium)"/>
        <rect x="230" y="200" width="80" height="890" rx="30" fill="url(#brushMedium)"/>
      </g>
      <rect class="label" x="70" y="646" width="216" height="300" rx="18" fill="var(--label)"/>
      <path class="ribbon" d="M70,810 L286,758 L286,838 L70,900 Z" fill="var(--ribbon)"/>
      <g class="claim">
        <path id="arcGripM" d="M89,912 A30,30 0 1 1 149,912" fill="none"/>
        <circle cx="119" cy="906" r="21" fill="var(--white)" stroke="var(--ink)" stroke-width="1.2"/>
        <rect x="104" y="909" width="30" height="4" rx="2" fill="none" stroke="var(--ink)"/>
        <rect x="104" y="901" width="9" height="7" fill="none" stroke="var(--ink)"/>
        <text class="claim-text" font-size="7.2"><textPath href="#arcGripM" startOffset="50%" text-anchor="middle">COMFORT GRIP HANDLE</textPath></text>
      </g>
      <g class="claim">
        <path id="arcTipM" d="M202,912 A30,30 0 1 1 262,912" fill="none"/>
        <circle cx="232" cy="906" r="21" fill="var(--white)" stroke="var(--ink)" stroke-width="1.2"/>
        <path d="M222,898 q10,-6 20,0 q2,10 -3,20 q-3,-6 -7,-6 q-4,0 -7,6 q-5,-10 -3,-20 Z" fill="none" stroke="var(--ink)" stroke-width="1.2"/>
        <text class="claim-text" font-size="6.4"><textPath href="#arcTipM" startOffset="50%" text-anchor="middle">SOFT &amp; SLIM TIP BRISTLES</textPath></text>
      </g>
    </svg>
    <div class="series"><div class="series-name">Feather Line<br>Medium</div><div class="series-soft">Soft</div></div>
    <div class="pack">3Pack</div>
    <div class="brand">GlintOn</div>
  </div>

</div>
</body>
</html>
```